Mailing Flyer for Fruit Box Company

Need to design a postcard (2 sides) with both sides completed which will be mailed to companies.

The flyer needs to represent the following point in a graphical way.

1. Our team has sophisticated experience and knowledge in the produce industry that will undoubtedly leave you satisfied.
2. We’ve collaborated with many of our finest local growers that of which have been around for numerous generations such as, Copper Hollow Orchards (GIVE MORE LOCAL GROWER EXAMPLES).
3. We have insight on the finest grown fruits; including great judgement as to when they will taste their best.
4. Our company guarantees you get the most superior fruits at the peak of their seasons.
5. With our trustworthy team you can depend on us to satisfy all of your wants and needs.
6. Our farmers grow sustainable produce to help ensure that our future ecosystem is at its absolute best.
7. We have the type of fruits that will not only leave your tastebuds and heart fulfilled, but will cause you to want more after every order.
8. We’ve performed a wholesale business with the farmers in order to grant our customers the freshest fruits at their best valued price.
9. Now that you're able to order from any location in the United States say goodbye to standing in long lines at the grocery stores.
10. Our complementary policy allows our customers to try your first box free of charge.

A summary of the above could be written as:
Our Harvest Lantern team has decades of expertise in the produce industry, which we utilize to make insightful decisions on the produce we provide for our customers. We have collaborated with the multi-generational farms such as Copper Hollow Orchards to guarantee we supply fruits at the peak of their season. We are an environmentally conscious business, and buy sustainable produce from local growers. When you buy a box from The Harvest Lantern you can say goodbye to standing in long lines at the grocery store, enjoy fresh fruit at their best valued price, and receive the first box free of charge.

The point is to illustrate the above, not to have a lot of text since no one reads.
One side is for the mailing so it should have a space to put a sticker for the mailing address to send the mail to.

Size should be 8.5 width x 5.5 high (21.5cm width x 14cm hight)
We will also provide you with the logo of the company (see attached)

Target Market(s)

Offices in the San Francisco Bay Area

Colors

Designer to choose colors to be used in the design.

Requirements
Must have
• Nice photos of Fruits, Fruit boxes, Maybe a nice office meeting room with a nice fruit box on the table, maybe a picture of a beautiful farm. Something inspiring.
• Need to illustrate that products and boxes are delivered to companies.
• Need to give a feeling that this is an Exclusive Service, with the most highest quality fruits and services
• Need to have project in JPG and a format which support edit from our side, with possible layers or vectors.

```html
<!DOCTYPE html>
<html lang="en">
<head>
<meta charset="utf-8">
<title>The Harvest Lantern – Postcard</title>
<link href="https://fonts.googleapis.com/css2?family=Cinzel:wght@700&family=Ubuntu:wght@400;500;700&display=swap" rel="stylesheet">
<style>
  :root {
    --backdrop: #44555f;
    --black: #000000;
    --white: #ffffff;
    --red: #b30a0a;
    --red-deep: #8e0606;
    --green: #3cb521;
    --green-dark: #2e7d1f;
    --ink: #1a1a1a;
    --stamp: #e3e3e3;
  }
  * { margin: 0; padding: 0; box-sizing: border-box; }
  html, body { width: 1200px; height: 1200px; overflow: hidden; }
  body { background: var(--backdrop); position: relative; font-family: "Ubuntu", sans-serif; }

  .card { position: absolute; width: 626px; height: 406px; background: var(--white); overflow: hidden; }

  /* Front */
  .card--front { left: 154px; top: 155px; }
  .front-photo {
    position: absolute; left: 0; top: 0; width: 440px; height: 153px;
    background:
      linear-gradient(90deg, rgba(255,255,255,0) 78%, #fff 100%),
      radial-gradient(circle at 30% 50%, #f1b13c 0 18%, transparent 40%),
      radial-gradient(circle at 70% 45%, #b0101e 0 20%, transparent 45%),
      linear-gradient(90deg, #d9522a 0%, #e9a03a 30%, #a8101c 60%, #c51a22 85%);
  }
  .brand { position: absolute; left: 450px; top: 36px; width: 160px; text-align: center; color: var(--green-dark); font-weight: 700; font-size: 17px; line-height: 1.2; }
  .brand__dot { display: block; width: 34px; height: 34px; border-radius: 50%; background: var(--green-dark); margin: 0 auto 8px; }
  .headline-band { position: absolute; left: 0; top: 153px; width: 100%; height: 45px; background: var(--black); display: flex; align-items: center; justify-content: center; }
  .headline { font-family: "Cinzel", serif; font-weight: 700; color: var(--green); font-size: 27px; letter-spacing: .5px; }
  .points { position: absolute; left: 0; top: 198px; width: 100%; height: 169px; background: linear-gradient(180deg, var(--red) 0%, var(--red-deep) 100%); display: flex; padding: 10px 18px 0 16px; }
  .points__col { list-style: none; width: 50%; }
  .points__col--left { padding-right: 14px; border-right: 1px solid rgba(0,0,0,.35); }
  .points__col--right { padding-left: 10px; }
  .point { display: flex; gap: 7px; color: var(--white); font-size: 8.3px; font-weight: 500; line-height: 1.33; margin-bottom: 7px; }
  .point__num { flex: 0 0 12px; height: 12px; border-radius: 50%; background: var(--green); color: var(--white); font-size: 7px; font-weight: 700; display: flex; align-items: center; justify-content: center; margin-top: -1px; }
  .site { position: absolute; left: 0; width: 100%; text-align: center; font-size: 12px; font-weight: 500; letter-spacing: 2.4px; color: var(--ink); }
  .card--front .site { top: 374px; }

  /* Back */
  .card--back { left: 420px; top: 640px; }
  .back-panel { position: absolute; left: 0; top: 0; width: 370px; height: 406px; clip-path: polygon(0 0, 354px 0, 287px 406px, 0 406px); }
  .about { position: absolute; left: 0; top: 0; width: 100%; height: 156px; background: var(--black); padding: 15px 20px 0 15px; }
  .about__title { color: var(--green); font-weight: 700; font-size: 19px; line-height: 1; margin-bottom: 4px; }
  .about__text { color: var(--white); font-size: 9.4px; line-height: 1.3; width: 325px; }
  .back-photo {
    position: absolute; left: 0; top: 156px; width: 100%; height: 202px;
    background: linear-gradient(180deg, #2f7fd6 0%, #8fc0ef 28%, #e7b23c 55%, #e07a1f 80%, #b2411a 100%);
  }
  .card--back .site { top: 362px; left: 0; width: 288px; }
  .stripe { position: absolute; left: 0; top: 0; }
  .brand--back { left: 400px; top: 22px; width: 120px; font-size: 12px; }
  .brand--back .brand__dot { width: 24px; height: 24px; margin-bottom: 5px; }
  .stamp { position: absolute; left: 566px; top: 16px; width: 45px; height: 46px; background: var(--stamp); }
  .address-line { position: absolute; left: 411px; width: 198px; height: 1.5px; background: var(--ink); }
</style>
</head>
<body>

<section class="card card--front">
  <div class="front-photo" role="img" aria-label="Wooden crate of peaches, apricots, cherries and strawberries"></div>
  <div class="brand"><span class="brand__dot"></span>The Harvest<br>Lantern</div>
  <div class="headline-band"><h1 class="headline">Bringing Farm Fresh Produce to You!</h1></div>
  <div class="points">
    <ol class="points__col points__col--left">
      <li class="point"><span class="point__num">1</span><span>Our team has sophisticated experience and knowledge in the produce industry that will undoubtedly leave you satisfied.</span></li>
      <li class="point"><span class="point__num">2</span><span>We’ve collaborated with many of our finest local growers that of which have been around for numerous generations such as, Copper Hollow Orchards (GIVE MORE LOCAL GROWER EXAMPLES).</span></li>
      <li class="point"><span class="point__num">3</span><span>We have insight on the finest grown fruits; including great judgement as to when they will taste their best.</span></li>
      <li class="point"><span class="point__num">4</span><span>Our company guarantees you get the most superior fruits at the peak of their seasons.</span></li>
      <li class="point"><span class="point__num">5</span><span>With our trustworthy team you can depend on us to satisfy all of your wants and needs.</span></li>
    </ol>
    <ol class="points__col points__col--right">
      <li class="point"><span class="point__num">6</span><span>Our farmers grow sustainable produce to help ensure that our future ecosystem is at its absolute best.</span></li>
      <li class="point"><span class="point__num">7</span><span>We have the type of fruits that will not only leave your tastebuds and heart fulfilled, but will cause you to want more after every order.</span></li>
      <li class="point"><span class="point__num">8</span><span>We’ve performed a wholesale business with the farmers in order to grant our customers the freshest fruits at their best valued price.</span></li>
      <li class="point"><span class="point__num">9</span><span>Now that you're able to order from any location in the United States say goodbye to standing in long lines at the grocery stores.</span></li>
      <li class="point"><span class="point__num">10</span><span>Our complementary policy allows our customers to try your first box free of charge.</span></li>
    </ol>
  </div>
  <p class="site">www.harvestlantern.com</p>
</section>

<section class="card card--back">
  <div class="back-panel">
    <div class="about">
      <h2 class="about__title">ABOUT US</h2>
      <p class="about__text">Our Harvest Lantern team has decades of expertise in the produce industry, which we utilize to make insightful decisions on the produce we provide for our customers. We have collaborated with the multi-generational farms such as Copper Hollow Orchards to guarantee we supply fruits at the peak of their season. We are an environmentally conscious business, and buy sustainable produce from local growers. When you buy a box from The Harvest Lantern you can say goodbye to standing in long lines at the grocery store, enjoy fresh fruit at their best valued price, and receive the first box free of charge.</p>
    </div>
    <div class="back-photo" role="img" aria-label="Wicker basket of mixed fruit under a blue sky"></div>
    <p class="site">www.harvestlantern.com</p>
  </div>
  <svg class="stripe" width="626" height="406" viewBox="0 0 626 406" aria-hidden="true">
    <polygon points="354,0 369,0 293,406 286,406" fill="var(--red)"/>
  </svg>
  <div class="brand brand--back"><span class="brand__dot"></span>The Harvest<br>Lantern</div>
  <div class="stamp"></div>
  <div class="address-line" style="top:196px"></div>
  <div class="address-line" style="top:221px"></div>
  <div class="address-line" style="top:245px"></div>
</section>

</body>
</html>
```